BOOK COVER (6 X 9) FOR CARNFIELD MOOR BOOKS

Book title: SEASONS OF GLASS; Author: TOMAS R. VELUNDE

This is the story of a man who grew up in Saudi Arabia in the 1940s, was schooled around the world. He survived death many times, once during the revolution in Bangladesh in the 1970s. Although a Pakistani, he knew Saudi royalty and worked there for most of his life. A lot of mystical things happened to him. SORRY TO BE SO VAGUE.

Book size will be 6 x 9

Target Market(s)

Adults interested in immigrant stories; the unexplainable; whimsical memoirs

Requirements
Nice to have
• This is a man who lived in many different worlds and countries. He lived through the Bangladesh revolution and other life threatening events.
Should not have
• Arabic dress -- he wore white suits

```html
<!DOCTYPE html>
<html lang="en">
<head>
<meta charset="utf-8">
<title>Seasons of Glass — Cover Wrap</title>
<link rel="stylesheet" href="https://fonts.googleapis.com/css2?family=Fjalla+One&family=Arimo:wght@700&display=swap">
<style>
  :root {
    --page-bg: #ececec;
    --back-grey: #a7a7a5;
    --spine-grey: #b9b9b7;
    --front-grey: #cbcbc8;
    --ink-green: #173a1e;
    --isbn-green: #0f2a14;
    --body-ink: #141a15;
    --leather-light: #9a4a36;
    --leather-dark: #5a2417;
  }
  * { box-sizing: border-box; margin: 0; padding: 0; }
  html, body { width: 1200px; height: 800px; overflow: hidden; }
  body { background: var(--page-bg); position: relative; }

  .cover-wrap {
    position: absolute; left: 175px; top: 100px;
    width: 850px; height: 600px; display: flex;
    box-shadow: 0 6px 24px rgba(0,0,0,0.18);
  }

  .back-cover {
    width: 400px; height: 600px; background: var(--back-grey);
    padding: 34px 34px 30px; position: relative;
  }
  .back-author {
    font-family: "Fjalla One", sans-serif; color: var(--ink-green);
    font-size: 11px; text-align: right; letter-spacing: 0.5px;
  }
  .back-title {
    font-family: "Fjalla One", sans-serif; color: var(--ink-green);
    font-size: 42px; line-height: 1; text-align: center; margin-top: 4px;
    white-space: nowrap;
  }
  .back-blurb {
    font-family: "Arimo", sans-serif; font-weight: 700; color: var(--body-ink);
    font-size: 9.6px; line-height: 13.2px; text-align: justify;
    margin-top: 12px; height: 330px; overflow: hidden;
    text-align-last: center;
  }
  .publisher-name {
    position: absolute; left: 34px; bottom: 42px;
    font-family: "Fjalla One", sans-serif; color: var(--ink-green);
    font-size: 15px; line-height: 19px; letter-spacing: 0.5px;
  }
  .isbn-box {
    position: absolute; right: 34px; bottom: 30px; width: 104px; height: 66px;
    background: var(--isbn-green); color: #c9c9c9;
    font-family: "Arimo", sans-serif; font-size: 9px;
    display: flex; align-items: center; justify-content: center;
  }

  .spine {
    width: 50px; height: 600px; background: var(--spine-grey);
    display: flex; align-items: center; justify-content: space-between;
    flex-direction: column; padding: 26px 0;
    border-left: 1px solid rgba(0,0,0,0.08); border-right: 1px solid rgba(0,0,0,0.08);
  }
  .spine-title, .spine-author {
    writing-mode: vertical-rl; font-family: "Fjalla One", sans-serif;
    color: var(--ink-green); white-space: nowrap;
  }
  .spine-title { font-size: 30px; letter-spacing: 1px; }
  .spine-author { font-size: 12px; letter-spacing: 1px; }

  .front-cover {
    width: 400px; height: 600px; background: var(--front-grey);
    position: relative; text-align: center;
  }
  .front-title {
    font-family: "Fjalla One", sans-serif; color: var(--ink-green);
    font-size: 48px; line-height: 1; padding-top: 46px;
    white-space: nowrap;
  }
  .luggage-art {
    position: absolute; left: 70px; top: 130px; width: 290px; height: 400px;
    background: radial-gradient(closest-side at 56% 50%, var(--leather-light) 0%, var(--leather-dark) 70%, rgba(203,203,200,0) 100%);
  }
  .front-author {
    position: absolute; left: 0; right: 0; bottom: 36px;
    font-family: "Fjalla One", sans-serif; color: var(--ink-green);
    font-size: 17px; letter-spacing: 1px;
  }
</style>
</head>
<body>
  <main class="cover-wrap">
    <section class="back-cover">
      <p class="back-author">TOMAS R. VELUNDE</p>
      <h2 class="back-title">SEASONS OF GLASS</h2>
      <p class="back-blurb">Lorem ipsum dolor sit amet, consectetur adipisicing elit, sed do eiusmod tempor incididunt ut labore et dolore magna aliqua. Ut enim ad minim veniam, quis nostrud exercitation. Lorem ipsum dolor sit amet, consectetur adipisicing elit, sed do eiusmod tempor incididunt ut labore et dolore magna aliqua. Ut enim ad minim veniam, quis nostrud exercitation. Lorem ipsum dolor sit amet, consectetur adipisicing elit, sed do eiusmod tempor incididunt ut labore et dolore magna aliqua. Ut enim ad minim veniam, quis nostrud exercitation. Lorem ipsum dolor sit amet, consectetur adipisicing elit, sed do eiusmod tempor incididunt ut labore et dolore magna aliqua. Ut enim ad minim veniam, quis nostrud exercitation. Lorem ipsum dolor sit amet, consectetur adipisicing elit, sed do eiusmod tempor incididunt ut labore et dolore magna aliqua. Ut enim ad minim veniam, quis nostrud exercitation. Lorem ipsum dolor sit amet, consectetur adipisicing elit, sed do eiusmod tempor incididunt ut labore et dolore magna aliqua. Ut enim ad minim veniam, quis nostrud exercitation. Lorem ipsum dolor sit amet, consectetur adipisicing elit, sed do eiusmod tempor incididunt ut labore et dolore magna aliqua. Ut enim ad minim veniam, quis nostrud exercitation. Lorem ipsum dolor sit amet, consectetur adipisicing elit, sed do eiusmod tempor incididunt ut labore et dolore magna aliqua. Ut enim ad minim veniam, quis nostrud exercitation. Lorem ipsum dolor sit amet, consectetur adipisicing elit, sed do eiusmod tempor incididunt ut labore et dolore magna aliqua. Ut enim ad minim veniam, quis nostrud exercitation.</p>
      <p class="publisher-name">CARNFIELD MOOR<br>BOOKS</p>
      <div class="isbn-box">ISBN</div>
    </section>

    <section class="spine">
      <span class="spine-title">SEASONS OF GLASS</span>
      <span class="spine-author">TOMAS R. VELUNDE</span>
    </section>

    <section class="front-cover">
      <h1 class="front-title">SEASONS OF GLASS</h1>
      <div class="luggage-art" role="img" aria-label="Photograph of a worn brown leather rolling suitcase bearing three national flag patches, with a matching leather toiletry bag beside it"></div>
      <p class="front-author">TOMAS R. VELUNDE</p>
    </section>
  </main>
</body>
</html>
```